BOLD & MINIMALIST DESIGN NEEDED

We want a very bold but minimalistic business card design that is impactful and utilizes both sides of the business card. Our current logo is included for your use.

We want bold fonts and good use of negative space. We don't want the logo to overpower the design.

Target Market(s)

Professionals who are building new commercial buildings.

Industry/Entity Type

Construction

Contact Information for Business Card

Name, Title, email, office phone, cell phone, website

Font styles to use
Serif
Sans Serif

Requirements
Must have
• Bold design!

```html
<!DOCTYPE html>
<html lang="en">
<head>
<meta charset="utf-8">
<title>Jonas Reed – Business Card</title>
<link rel="stylesheet" href="https://fonts.googleapis.com/css2?family=Montserrat:wght@600;700;800&display=swap">
<style>
  :root {
    --brand-green: #86c226;
    --card-green: #8dc63f;
    --card-white: #ffffff;
    --ink: #111111;
    --shadow: rgba(0, 0, 0, 0.35);
  }
  * { margin: 0; padding: 0; box-sizing: border-box; }
  html, body { width: 1200px; height: 1200px; overflow: hidden; }
  body {
    background: var(--brand-green);
    position: relative;
    font-family: "Montserrat", Arial, sans-serif;
  }
  .card {
    position: absolute;
    left: 206px;
    width: 790px;
    height: 453px;
    background: var(--card-white);
    box-shadow: 0 6px 18px var(--shadow);
    overflow: hidden;
  }
  .card--front { top: 125px; }
  .card--back { top: 622px; }

  .front-header {
    position: absolute;
    left: 0; top: 0;
    width: 100%;
    height: 227px;
    background: var(--card-green);
  }
  .person-name {
    position: absolute;
    right: 158px;
    top: 62px;
    font-weight: 800;
    font-size: 58px;
    letter-spacing: 0.5px;
    color: var(--card-white);
    text-transform: uppercase;
    white-space: nowrap;
  }
  .title-rule {
    position: absolute;
    left: 158px;
    top: 144px;
    width: 281px;
    height: 2px;
    background: var(--card-white);
  }
  .person-title {
    position: absolute;
    right: 158px;
    top: 128px;
    font-weight: 700;
    font-size: 26px;
    letter-spacing: 0.5px;
    color: var(--card-white);
    text-transform: uppercase;
  }

  .contact-list {
    position: absolute;
    left: 156px;
    top: 258px;
    list-style: none;
  }
  .contact-item {
    display: flex;
    align-items: center;
    height: 23px;
    margin-bottom: 22.5px;
    font-weight: 700;
    font-size: 20px;
    color: var(--ink);
  }
  .contact-item--address { text-transform: uppercase; font-size: 19px; }
  .contact-icon {
    width: 22px;
    height: 22px;
    margin-right: 21px;
    flex: none;
  }

  .company-mark {
    position: absolute;
    left: 0; top: 0;
    width: 100%; height: 100%;
    display: flex;
    flex-direction: column;
    align-items: center;
    justify-content: center;
  }
  .company-name {
    display: flex;
    align-items: center;
    gap: 14px;
    font-weight: 800;
    font-size: 44px;
    letter-spacing: 1px;
    color: var(--ink);
    text-transform: uppercase;
  }
  .company-square {
    width: 26px;
    height: 26px;
    background: var(--card-green);
  }
</style>
</head>
<body>

  <section class="card card--front">
    <div class="front-header">
      <h1 class="person-name">Jonas Reed</h1>
      <div class="title-rule"></div>
      <p class="person-title">Architect</p>
    </div>

    <ul class="contact-list">
      <li class="contact-item">
        <svg class="contact-icon" viewBox="0 0 22 22" aria-hidden="true">
          <circle cx="11" cy="11" r="11" fill="var(--card-green)"/>
          <path d="M7.2 6.2l2 .2 1 2.3-1.2 1a6 6 0 0 0 3.3 3.3l1-1.2 2.3 1 .2 2c-.3.6-.9.9-1.6.9A8.6 8.6 0 0 1 6.3 7.8c0-.7.3-1.3.9-1.6z" fill="#fff"/>
        </svg>
        555 014 2763
      </li>
      <li class="contact-item">
        <svg class="contact-icon" viewBox="0 0 22 22" aria-hidden="true">
          <circle cx="11" cy="11" r="11" fill="var(--card-green)"/>
          <rect x="6" y="7.5" width="10" height="7" fill="#fff"/>
          <path d="M6 7.5l5 4 5-4" fill="none" stroke="var(--card-green)" stroke-width="1"/>
        </svg>
        info@jonasreed.com
      </li>
      <li class="contact-item">
        <svg class="contact-icon" viewBox="0 0 22 22" aria-hidden="true">
          <circle cx="11" cy="11" r="11" fill="var(--card-green)"/>
          <g fill="none" stroke="#fff" stroke-width="1.1">
            <circle cx="11" cy="11" r="5"/>
            <ellipse cx="11" cy="11" rx="2.2" ry="5"/>
            <path d="M6 11h10M6.8 8.5h8.4M6.8 13.5h8.4"/>
          </g>
        </svg>
        www.jonasreed.com
      </li>
      <li class="contact-item contact-item--address">
        <svg class="contact-icon" viewBox="0 0 22 22" aria-hidden="true">
          <circle cx="11" cy="11" r="11" fill="var(--card-green)"/>
          <path d="M11 16.5s-4-4.2-4-7a4 4 0 0 1 8 0c0 2.8-4 7-4 7z" fill="#fff"/>
          <circle cx="11" cy="9.5" r="1.5" fill="var(--card-green)"/>
        </svg>
        Maple Court Suite, Eastford
      </li>
    </ul>
  </section>

  <section class="card card--back">
    <div class="company-mark">
      <p class="company-name"><span class="company-square"></span>Ridgeline Design + Build</p>
    </div>
  </section>

</body>
</html>
```